Honigmüsli Etikett
Zielgruppe
Wir sind eine Imkerei und erzeugen Regionale, Nachhaltige und Biologisch wertvolle Produkte bei denen die umwelt und der umweltschutz sowie die Qualität im vordergrund stehen.
Aufgabenstellung
Der Kunde soll die Natührlichkeit des Produktes im Etikett erkennen.
Es handelt sich hierbei um eine Müslitüte aus braunem Papier mit großem Sichtfenster.
Das Frontetikett sollte nur die wichtigsten und prignanten Dinge aufweisen und das Rückenetikett dann die restlichen Dinge.
Im anhang befindet sich bereits das aktuelle Etikett, welches so im moment auf den Tüten zu sehen ist. Dieses soll nun aber modernisiert und aufgefrischt werden.
Es handelt sich um ein mit Honig gesüßtes Müsli, welches ausschließlich auf gesunde und natührliche Stoffe setzt, dies soll im Etikett wiedergespiegelt werden.
Die Etiketten sind derzeit in den Maßen: 7,5cm x 5cm (Front) und 8,5cm x 6cm (Rücken)
dies ist aber kein muss und kann wenn es möglichkeiten der Etikettgestaltungen gibt die mehr Platz benötigen auch angepasst werden. Das Gesamtbild mit dem großen Fenster sollte allerdings harmonieren und nicht durch ein zu großes Etikett überlagert werden.

```html
<!DOCTYPE html>
<html lang="de">
<head>
<meta charset="utf-8">
<title>Knuspermüsli Etikett – Front und Rücken</title>
<link href="https://fonts.googleapis.com/css2?family=Jost:wght@400;500;600&family=Pinyon+Script&display=swap" rel="stylesheet">
<style>
  :root {
    --honey: #eabb3b;
    --mint: #5cbb9c;
    --mint-pale: #d8f3e8;
    --charcoal: #3a3a3a;
    --ink: #222222;
    --white: #ffffff;
  }
  * { margin: 0; padding: 0; box-sizing: border-box; }
  html, body {
    width: 1200px; height: 830px; overflow: hidden;
    background: var(--white);
    font-family: "Jost", sans-serif;
  }
  .canvas { position: relative; width: 1200px; height: 830px; }

  /* Front label */
  .front-label {
    position: absolute; left: 107px; top: 123px;
    width: 408px; height: 610px;
    background: var(--honey); overflow: hidden;
  }
  .front-band {
    position: absolute; left: 0; width: 100%;
    background: var(--charcoal); color: var(--white);
    font-size: 15.5px; font-weight: 500;
    display: flex; align-items: center; justify-content: center;
  }
  .front-band--top { top: 0; height: 89px; padding-top: 28px; }
  .front-band--bottom { bottom: 0; height: 46px; }
  .ornament-area {
    position: absolute; left: 46px; top: 142px;
    width: 318px; height: 318px; border-radius: 50%;
    background: radial-gradient(circle, rgba(255,255,255,0.28) 0%, rgba(255,255,255,0.12) 60%, rgba(234,187,59,0) 72%);
  }
  .quatrefoil { position: absolute; left: 0; top: 0; }
  .brand-mark {
    position: absolute; left: 0; width: 100%; top: 186px;
    display: flex; flex-direction: column; align-items: center;
  }
  .brand-mark__circle {
    width: 40px; height: 40px; border-radius: 50%;
    border: 2px solid var(--ink);
  }
  .brand-mark__name {
    margin-top: 4px; font-size: 8px; font-weight: 500; color: var(--ink);
  }
  .product-title {
    position: absolute; left: 0; width: 100%; top: 258px;
    text-align: center; font-family: "Pinyon Script", cursive;
    font-size: 36px; line-height: 34px; color: var(--charcoal);
  }
  .product-claim {
    position: absolute; left: 0; width: 100%; top: 333px;
    text-align: center; font-size: 15.5px; color: var(--white);
  }
  .product-weight {
    position: absolute; left: 182px; top: 381px; width: 46px;
    border-top: 1px solid var(--white); border-bottom: 1px solid var(--white);
    text-align: center; color: var(--white);
    font-size: 15.5px; line-height: 29px;
  }

  /* Back label */
  .back-label {
    position: absolute; left: 607px; top: 41px;
    width: 488px; height: 692px;
    background: var(--honey); overflow: hidden;
  }
  .corner-decor { position: absolute; border-radius: 50%; }
  .corner-decor--top {
    right: -40px; top: -40px; width: 200px; height: 200px;
    background: radial-gradient(circle, rgba(255,255,255,0.22) 0%, rgba(234,187,59,0) 70%);
  }
  .corner-decor--bottom {
    left: -50px; bottom: -70px; width: 220px; height: 220px;
    background: radial-gradient(circle, rgba(255,255,255,0.22) 0%, rgba(234,187,59,0) 70%);
  }
  .info-panel {
    position: absolute; left: 40px; top: 40px;
    width: 408px; height: 611px;
    background: var(--mint); border: 5px solid var(--mint-pale);
  }
  .info-panel__inner { position: absolute; left: 58px; top: 0; width: 290px; }
  .ingredients-heading {
    position: absolute; top: 61px; font-size: 21px; font-weight: 600; color: var(--white);
  }
  .ingredients-list {
    position: absolute; top: 92px; width: 300px;
    font-size: 22px; line-height: 27.5px; color: var(--white);
  }
  .ingredients-note {
    position: absolute; top: 207px; font-size: 15px; color: var(--ink);
  }
  .rule { position: absolute; left: 0; width: 282px; border-top: 1px solid var(--charcoal); }
  .rule--upper { top: 241px; }
  .rule--lower { top: 383px; }
  .best-before {
    position: absolute; top: 254px; font-size: 14px; font-weight: 600; color: var(--ink);
  }
  .producer-address {
    position: absolute; top: 402px; font-size: 21px; line-height: 27.5px;
    color: var(--ink); font-style: normal;
  }
  .producer-web {
    position: absolute; top: 553px; left: 6px;
    font-size: 21px; font-weight: 600; color: var(--ink); white-space: nowrap;
  }
</style>
</head>
<body>
<div class="canvas">

  <section class="front-label">
    <div class="front-band front-band--top">Honig aus eigener Imkerei</div>

    <div class="ornament-area" role="img" aria-label="Dekoratives Muster aus gepunkteten Kreisen in Weiß und Dunkelgrau"></div>

    <svg class="quatrefoil" width="408" height="610" viewBox="0 0 408 610" aria-hidden="true">
      <g fill="var(--mint-pale)">
        <circle cx="204" cy="230" r="75"/>
        <circle cx="204" cy="372" r="75"/>
        <circle cx="133" cy="301" r="75"/>
        <circle cx="275" cy="301" r="75"/>
      </g>
      <g fill="var(--mint)">
        <circle cx="204" cy="230" r="70"/>
        <circle cx="204" cy="372" r="70"/>
        <circle cx="133" cy="301" r="70"/>
        <circle cx="275" cy="301" r="70"/>
        <rect x="131" y="228" width="146" height="146"/>
      </g>
    </svg>

    <div class="brand-mark">
      <div class="brand-mark__circle"></div>
      <div class="brand-mark__name">Bienenhof Kräuter</div>
    </div>

    <h1 class="product-title">Kräuter<br>Knuspermüsli</h1>
    <p class="product-claim">mit Honig veredelt</p>
    <p class="product-weight">500 g</p>

    <div class="front-band front-band--bottom">Hergestell in unserer Manufaktur</div>
  </section>

  <section class="back-label">
    <div class="corner-decor corner-decor--top" role="img" aria-label="Dekorative gepunktete Kreisbögen"></div>
    <div class="corner-decor corner-decor--bottom" role="img" aria-label="Dekorative gepunktete Kreisbögen"></div>

    <div class="info-panel">
      <div class="info-panel__inner">
        <h2 class="ingredients-heading">Zutaten:</h2>
        <p class="ingredients-list">Haferflocken, Honig<br>Sonnenblumenkerne, Öl<br>Mandeln, Rosinen<br>getrocknete Weinblätter</p>
        <p class="ingredients-note">ohne künstliche Zusatzstoffe</p>
        <div class="rule rule--upper"></div>
        <p class="best-before">Mindestens haltbar bis:</p>
        <div class="rule rule--lower"></div>
        <address class="producer-address">Bienenhof Kräuter<br>Lindenweg 7<br>34100 Talheim<br>01234 | 567890</address>
        <p class="producer-web">www.bienenhof-kraeuter.de</p>
      </div>
    </div>
  </section>

</div>
</body>
</html>
```